The Tidy Lantern Business Card

I need a business card designed for The Tidy Lantern. The company provides on site support and education to end consumers in the ins and outs of all our digital devices. We advise on product purchase, installation, maintenance and troubleshooting. Anything from cordless phones to home networks.
My initial concept is double sided with the white logo on green on one side and contact details and a small logo on the flip side (logo package attached)
Contact Details:
Miles Fenwright
Managing Director
PO Box 43
Brackton, NSW 2187
Phone: 0438 907 516
email: miles@tidylantern.com.au
web: www.tidylantern.com.au
Target Market(s)
Busy professionals and retired folks.
Industry/Entity Type
Education
Look and feel

```html
<!DOCTYPE html>
<html lang="en">
<head>
<meta charset="utf-8">
<title>The Tidy Lantern – Business Card</title>
<link rel="stylesheet" href="https://fonts.googleapis.com/css2?family=Open+Sans:wght@400&display=swap">
<style>
  :root {
    --board: #152c42;
    --card: #f7f7f6;
    --navy: #1b2b3e;
    --green: #7ab342;
    --label: #f2f4f6;
  }
  html, body {
    margin: 0;
    padding: 0;
    overflow: hidden;
  }
  .board {
    position: relative;
    width: 1200px;
    height: 1000px;
    background: var(--board);
    font-family: "Open Sans", Verdana, sans-serif;
    overflow: hidden;
  }
  .side-label {
    position: absolute;
    margin: 0;
    color: var(--label);
    font-size: 82px;
    font-weight: 400;
    line-height: 1;
  }
  .side-label--front { left: 43px; top: 145px; }
  .side-label--back { left: 55px; top: 665px; }

  .card {
    position: absolute;
    left: 360px;
    width: 687px;
    background: var(--card);
  }
  .card--front { top: 39px; height: 397px; }
  .card--back { top: 522px; height: 405px; }

  .brand {
    position: absolute;
    display: flex;
    align-items: center;
    color: var(--navy);
    font-weight: 400;
    white-space: nowrap;
  }
  .brand__dot {
    flex: none;
    border-radius: 50%;
    background: var(--green);
  }
  .card--front .brand {
    left: 108px;
    top: 190px;
    font-size: 44px;
    gap: 20px;
  }
  .card--front .brand__dot { width: 56px; height: 56px; }

  .card--back .brand {
    left: 338px;
    top: 100px;
    font-size: 30px;
    gap: 14px;
  }
  .card--back .brand__dot { width: 38px; height: 38px; }

  .contact {
    position: absolute;
    left: 58px;
    top: 214px;
    margin: 0;
    padding: 0;
    list-style: none;
    font-size: 23px;
    line-height: 1;
  }
  .contact__row {
    display: flex;
    gap: 12px;
    height: 37px;
    align-items: center;
  }
  .contact__row + .contact__row { margin-top: 2px; }
  .contact__key { color: var(--green); }
  .contact__value { color: var(--navy); }
  .contact__value .domain { color: var(--green); }
</style>
</head>
<body>
<main class="board">
  <h2 class="side-label side-label--front">front</h2>
  <h2 class="side-label side-label--back">back</h2>

  <section class="card card--front" aria-label="Card front">
    <div class="brand">
      <span class="brand__dot" aria-hidden="true"></span>
      <span class="brand__name">The Tidy Lantern</span>
    </div>
  </section>

  <section class="card card--back" aria-label="Card back">
    <div class="brand">
      <span class="brand__dot" aria-hidden="true"></span>
      <span class="brand__name">The Tidy Lantern</span>
    </div>
    <ul class="contact">
      <li class="contact__row"><span class="contact__key">po box</span><span class="contact__value">43 Brackton, NSW 2187</span></li>
      <li class="contact__row"><span class="contact__key">phone</span><span class="contact__value">0438 907 516</span></li>
      <li class="contact__row"><span class="contact__key">web</span><span class="contact__value">www.tidylantern.com.au</span></li>
      <li class="contact__row"><span class="contact__key">email</span><span class="contact__value">miles@<span class="domain">tidylantern.com.au</span></span></li>
    </ul>
  </section>
</main>
</body>
</html>
```